Wholesale in Gold Jewellery & Gold Bullion

We are an established gold jewellery and gold bullion wholesaler selling these products to international clients. We already have a name and logo of our company, hence please view attached current card design. We need a completely new design to compliment our business and industry and the final design should be new and elegant.

Contact Information for Business Card

New card details must be same as per current card. Like logo, name, tel no. & etc.

Colors

Designer to choose colors to be used in the design.

```html
<!DOCTYPE html>
<html lang="en">
<head>
<meta charset="utf-8">
<title>Kestrel &amp; Co Pte Ltd – Business Card</title>
<link rel="stylesheet" href="https://fonts.googleapis.com/css2?family=Lato:wght@400;700&family=Tinos:wght@700&display=swap">
<style>
  :root {
    --backdrop: #e4e5e7;
    --card: #ffffff;
    --gold: #f0a125;
    --gold-deep: #e0911a;
    --ink: #111111;
  }
  html, body {
    margin: 0;
    width: 1200px;
    height: 800px;
    overflow: hidden;
    background: var(--backdrop);
  }
  .card {
    position: absolute;
    left: 150px;
    top: 143px;
    width: 900px;
    height: 514px;
    background: var(--card);
    box-shadow: 0 10px 30px rgba(0,0,0,0.12);
    overflow: hidden;
    font-family: "Lato", sans-serif;
    color: var(--ink);
  }
  .company-name {
    position: absolute;
    right: 44px;
    top: 34px;
    margin: 0;
    font-family: "Tinos", serif;
    font-weight: 700;
    font-size: 46px;
    letter-spacing: 1px;
  }
  .person {
    position: absolute;
    left: 40px;
    top: 108px;
    padding-left: 22px;
    border-left: 8px solid var(--gold);
  }
  .person-name {
    margin: 0;
    font-size: 36px;
    font-weight: 400;
    line-height: 1.05;
  }
  .person-role {
    margin: 0;
    font-size: 27px;
    line-height: 1.1;
  }
  .rules {
    position: absolute;
    left: 0;
    top: 0;
  }
  .mark {
    position: absolute;
    left: 575px;
    top: 226px;
    display: flex;
    align-items: center;
    gap: 12px;
    background: var(--card);
    padding: 6px 10px;
  }
  .mark-dot {
    width: 30px;
    height: 30px;
    border-radius: 50%;
    background: var(--gold);
  }
  .mark-name {
    font-size: 30px;
    font-weight: 700;
    color: var(--gold);
    letter-spacing: 1px;
  }
  .contacts {
    position: absolute;
    left: 40px;
    top: 290px;
    margin: 0;
    padding: 0;
    list-style: none;
    font-size: 25px;
    line-height: 36px;
  }
  .contacts li {
    display: flex;
    align-items: center;
    gap: 12px;
  }
  .contacts svg {
    width: 22px;
    height: 22px;
    fill: none;
    stroke: var(--gold);
    stroke-width: 2.2;
    stroke-linecap: round;
    stroke-linejoin: round;
  }
  .address {
    position: absolute;
    right: 40px;
    top: 376px;
    margin: 0;
    font-style: normal;
    font-size: 27px;
    line-height: 1.2;
    text-align: left;
  }
  .base-band {
    position: absolute;
    left: 0;
    bottom: 0;
    width: 100%;
    height: 32px;
    background: var(--gold-deep);
  }
</style>
</head>
<body>
  <section class="card">
    <h1 class="company-name">KESTREL &amp; CO PTE LTD</h1>

    <div class="person">
      <p class="person-name">Rohan Varadan</p>
      <p class="person-role">Director</p>
    </div>

    <svg class="rules" width="900" height="514" aria-hidden="true">
      <line x1="30" y1="238" x2="900" y2="238" stroke="var(--gold)" stroke-width="3"/>
      <line x1="30" y1="262" x2="900" y2="262" stroke="var(--gold)" stroke-width="3"/>
    </svg>

    <div class="mark">
      <span class="mark-dot"></span>
      <span class="mark-name">KESTREL &amp; CO</span>
    </div>

    <ul class="contacts">
      <li>
        <svg viewBox="0 0 24 24" aria-hidden="true"><path d="M5 3h4l2 5-3 2a11 11 0 0 0 6 6l2-3 5 2v4a2 2 0 0 1-2 2A17 17 0 0 1 3 5a2 2 0 0 1 2-2z"/></svg>
        +65 6100 2000
      </li>
      <li>
        <svg viewBox="0 0 24 24" aria-hidden="true"><rect x="7" y="2" width="10" height="20" rx="2"/><line x1="11" y1="18" x2="13" y2="18"/></svg>
        +65 9100 3456
      </li>
      <li>
        <svg viewBox="0 0 24 24" aria-hidden="true"><rect x="7" y="3" width="10" height="6"/><rect x="3" y="9" width="18" height="8" rx="1"/><rect x="7" y="14" width="10" height="7"/></svg>
        +65 6100 2001
      </li>
      <li>
        <svg viewBox="0 0 24 24" aria-hidden="true"><rect x="2" y="5" width="20" height="14"/><path d="M2 5l10 8 10-8"/></svg>
        rohan@kestrelco.com
      </li>
    </ul>

    <address class="address">12 Lantern Lane,<br>Singapore 100123</address>

    <div class="base-band"></div>
  </section>
</body>
</html>
```